Business Card Designs

Looking to design a 3.5" x 2" standard business card for our employees.
The design needs to be sleek, simple, and modern. We would like our logo (attached) to be incorporated, but not in that colour, rather an outline of the logo in either gold or silver (whichever looks better).

Modern and Simple is what we are looking for, but be creative in incorporating the logo.

```html
<!DOCTYPE html>
<html lang="en">
<head>
<meta charset="UTF-8">
<title>Business Card Designs</title>
<link href="https://fonts.googleapis.com/css2?family=Montserrat:wght@400;500;700&display=swap" rel="stylesheet">
<style>
  :root {
    --page-bg: #2b2b2b;
    --card-black: #141414;
    --gold-light: #f0dfb4;
    --gold-mid: #d6bd84;
    --gold-deep: #b89a5c;
    --text-white: #f4f4f4;
    --text-black: #111111;
  }
  * { box-sizing: border-box; margin: 0; padding: 0; }
  html, body { width: 1200px; height: 1200px; overflow: hidden; }
  body {
    background: var(--page-bg);
    font-family: 'Montserrat', sans-serif;
    position: relative;
  }
  .card {
    position: absolute;
    left: 250px;
    width: 700px;
    height: 400px;
    background: var(--card-black);
    border-radius: 28px;
    overflow: hidden;
    box-shadow: 0 0 0 3px var(--gold-deep);
  }
  .card-front { top: 130px; }
  .card-back { top: 670px; }

  .gold-band {
    position: absolute;
    left: 0;
    top: 140px;
    width: 470px;
    height: 62px;
    background: linear-gradient(90deg, var(--gold-deep), var(--gold-light) 45%, var(--gold-mid));
  }
  .brand-mark {
    position: absolute;
    left: 490px;
    top: 142px;
    font-weight: 700;
    font-size: 46px;
    letter-spacing: 3px;
    color: var(--gold-mid);
    line-height: 1;
  }
  .holder {
    position: absolute;
    left: 130px;
    top: 146px;
    color: var(--text-black);
  }
  .holder-name {
    font-weight: 700;
    font-size: 38px;
    letter-spacing: 1px;
    line-height: 1;
  }
  .holder-role {
    font-weight: 500;
    font-size: 15px;
    letter-spacing: 1px;
    margin-top: 2px;
  }
  .contact-list {
    position: absolute;
    left: 150px;
    top: 236px;
    list-style: none;
  }
  .contact-item {
    display: flex;
    align-items: center;
    gap: 16px;
    color: var(--text-white);
    font-size: 22px;
    font-weight: 400;
    height: 38px;
  }
  .contact-icon { width: 24px; height: 24px; flex: none; }

  .back-brand {
    position: absolute;
    inset: 0;
    display: flex;
    align-items: center;
    justify-content: center;
    gap: 22px;
  }
  .back-brand-dot {
    width: 34px;
    height: 34px;
    background: var(--gold-mid);
  }
  .back-brand-name {
    font-weight: 700;
    font-size: 84px;
    letter-spacing: 8px;
    color: var(--gold-mid);
    line-height: 1;
  }
</style>
</head>
<body>
  <section class="card card-front">
    <div class="gold-band"></div>
    <div class="brand-mark">TELLAR</div>
    <div class="holder">
      <p class="holder-name">JOHN DOE</p>
      <p class="holder-role">POSITION</p>
    </div>
    <ul class="contact-list">
      <li class="contact-item">
        <svg class="contact-icon" viewBox="0 0 24 24"><path fill="#d6bd84" d="M6.6 10.8a15 15 0 0 0 6.6 6.6l2.2-2.2c.3-.3.7-.4 1-.2 1.1.4 2.3.6 3.6.6.6 0 1 .4 1 1V20c0 .6-.4 1-1 1A17 17 0 0 1 3 4c0-.6.4-1 1-1h3.5c.6 0 1 .4 1 1 0 1.3.2 2.5.6 3.6.1.3 0 .7-.2 1z"/></svg>
        <span>(000) 000 0000</span>
      </li>
      <li class="contact-item">
        <svg class="contact-icon" viewBox="0 0 24 24"><rect x="2" y="5" width="20" height="14" fill="#d6bd84"/><path d="M2 5l10 8 10-8M2 19l7-7M22 19l-7-7" stroke="#141414" stroke-width="1.6" fill="none"/></svg>
        <span>email@yourwebsite.com</span>
      </li>
      <li class="contact-item">
        <svg class="contact-icon" viewBox="0 0 24 24" fill="none" stroke="#d6bd84" stroke-width="1.6"><circle cx="12" cy="12" r="10"/><ellipse cx="12" cy="12" rx="4.5" ry="10"/><path d="M2 12h20M4 7h16M4 17h16"/></svg>
        <span>www.youremail.com</span>
      </li>
    </ul>
  </section>

  <section class="card card-back">
    <div class="back-brand">
      <span class="back-brand-dot"></span>
      <span class="back-brand-name">TELLAR</span>
    </div>
  </section>
</body>
</html>
```